KorvanVista.com

Complete Website Design (Godaddy) and company Branding / Logo Design. The products will sell are only done in-person and are installed. So this site does not need to be an e-commerce site. We will only be giving out information and collecting customer inquires. Website will only need to be about 3 to 5 pages.

```html
<!DOCTYPE html>
<html lang="en">
<head>
<meta charset="utf-8">
<title>KorvanVista – HD TV Installations</title>
<link href="https://fonts.googleapis.com/css2?family=Montserrat:wght@400;500;600;700&family=Poppins:wght@700;800&family=Oswald:wght@500&display=swap" rel="stylesheet">
<style>
:root{
  --bg:#000;
  --red:#e32121;
  --white:#fff;
  --muted:#a9a9a9;
  --dim:#6f6f6f;
  --ghost:#111;
  --search:#fff;
}
*{margin:0;padding:0;box-sizing:border-box}
html,body{width:1200px;height:3220px;overflow:hidden;background:var(--bg)}
body{position:relative;font-family:"Montserrat",sans-serif;color:var(--white)}
.abs{position:absolute}
.display{font-family:"Poppins",sans-serif;font-weight:800}
.brand{font-family:"Poppins",sans-serif;font-weight:800;color:var(--red);font-size:24px;letter-spacing:-.3px}

/* nav */
.nav-links{left:443px;top:29px;display:flex;gap:30px;font-size:12px}
.nav-links a{color:var(--white);text-decoration:none;position:relative}
.nav-links a.active::after{content:"";position:absolute;left:0;right:0;bottom:-8px;height:2px;background:var(--red)}
.btn{background:var(--red);color:var(--white);border-radius:6px;display:flex;align-items:center;justify-content:center;font-size:12px;font-weight:500}
.call{left:1012px;top:22px;width:88px;height:30px;font-size:12px}

/* hero */
.hero-title{left:100px;top:202px;font-size:42px;line-height:60px}
.hero-copy{left:100px;top:325px;width:410px;font-size:15.5px;line-height:25px}
.get-started{left:100px;top:432px;width:150px;height:37px}
.learn{left:275px;top:442px;font-size:12px;display:flex;align-items:center;gap:12px}
.learn span{text-decoration:underline}
.stats{left:100px;top:500px;display:flex}
.stat .num{font-family:"Oswald",sans-serif;color:var(--red);font-size:26px;line-height:36px}
.stat .lbl{font-size:15px;margin-top:4px}
.hero-img{left:693px;top:171px;width:460px;height:335px;background:linear-gradient(135deg,#d9d2c6 0%,#b89b78 45%,#6b5036 80%,#3d2c1e 100%)}
.search{left:610px;top:506px;width:496px;height:58px;background:var(--search);border-radius:6px}
.search .ph{position:absolute;left:20px;top:22px;font-size:11px;color:#9a9a9a}
.find{position:absolute;left:386px;top:10px;width:100px;height:36px;font-size:12px;font-weight:700;gap:6px}

/* partners */
.partner-title{left:100px;top:722px;font-size:20px;font-weight:700}
.partner-copy{left:100px;top:756px;width:260px;font-size:12px;line-height:20px;color:var(--dim)}
.logo-row{top:744px;font-size:23px;font-weight:700;color:#9b9b9b;display:flex;align-items:center;gap:8px}
.logo-row i{display:inline-block;width:20px;height:20px;background:#9b9b9b}

/* about */
.about-ring{left:158px;top:898px;width:380px;height:380px;border-radius:50%;border:1.5px solid #d8d8d8}
.about-img{left:176px;top:898px;width:362px;height:362px;border-radius:50%;background:radial-gradient(circle at 45% 40%,#3f7fa6 0%,#1f4e6e 45%,#15293a 80%,#0b1218 100%)}
.about-title{left:678px;top:880px;font-size:25px}
.about-title em{font-style:normal;color:var(--red)}
.about-body{left:678px;top:937px;width:400px;font-size:10.6px;line-height:22.5px}
.about-body b{font-weight:700}
.about-body ul{list-style:none}
.about-body li{padding-left:17px;position:relative}
.about-body li::before{content:"";position:absolute;left:6px;top:10px;width:3px;height:3px;border-radius:50%;background:var(--white)}
.about-btn{left:678px;top:1267px;width:112px;height:39px;font-size:10px;font-weight:700;box-shadow:0 4px 14px rgba(227,33,33,.45)}

/* why */
.why-title{left:0;width:1182px;text-align:center;top:1462px;font-size:31px}
.card{top:1598px;width:260px}
.card .icon{width:75px;height:75px;background:var(--red);border-radius:6px;display:flex;align-items:center;justify-content:center}
.card h3{font-family:"Poppins",sans-serif;font-weight:800;font-size:15px;margin-top:20px}
.card p{font-size:11.5px;line-height:22.5px;color:var(--muted);margin-top:12px}

/* reviews */
.ghost{left:0;width:1270px;text-align:center;top:1900px;font-size:100px;color:var(--ghost);letter-spacing:1px}
.review-ring{left:109px;top:2031px;width:394px;height:394px;border-radius:50%;border:1.5px solid #3a3a3a}
.review-img{left:148px;top:2058px;width:340px;height:340px;border-radius:50%;background:radial-gradient(circle at 40% 35%,#f4a6d6 0%,#b45ad8 40%,#5b3fd0 70%,#2b2f8c 100%)}
.review-title{left:638px;top:2065px;font-size:31px;line-height:43px}
.review-copy{left:638px;top:2181px;width:380px;font-size:15.5px;line-height:30px;font-weight:600}
.author{left:638px;top:2316px;font-size:11px}
.arrow{top:2367px;width:22px;height:22px;border-radius:50%;display:flex;align-items:center;justify-content:center}

/* cta */
.cta{left:156px;top:2583px;width:888px;height:219px;background:var(--red);border-radius:8px}
.cta-text{position:absolute;left:61px;top:52px;width:580px;font-size:24px;line-height:38px;font-weight:700}
.cta-text span{text-decoration:underline;text-decoration-color:#f2a13a;text-decoration-thickness:3px;text-underline-offset:5px}
.cta-btn{position:absolute;left:644px;top:72px;width:119px;height:43px;background:#000;border-radius:4px;font-size:10px;font-weight:600;display:flex;align-items:center;justify-content:center;box-shadow:0 3px 8px rgba(0,0,0,.35)}

/* footer */
.foot-brand{left:156px;top:2930px;font-size:22px}
.foot-tag{left:156px;top:2971px;width:170px;font-size:10px;line-height:19px}
.socials{left:158px;top:3037px;display:flex;gap:8px}
.socials i{display:block;width:22px;height:22px;border-radius:50%;background:#2a0d0d}
.copyright{left:156px;top:3088px;font-size:10px}
.fcol{top:2942px;font-size:10px}
.fcol h4{font-family:"Poppins",sans-serif;font-weight:800;font-size:12px;margin-bottom:21px}
.fcol li{list-style:none;margin-bottom:16px}
</style>
</head>
<body>

<header>
  <div class="abs brand" style="left:100px;top:18px">KorvanVista</div>
  <nav class="abs nav-links">
    <a class="active" href="#">Home</a><a href="#">Service</a><a href="#">Pricing</a><a href="#">Blog</a><a href="#">About Us</a>
  </nav>
  <div class="abs btn call">Call us</div>
</header>

<section class="hero">
  <h1 class="abs display hero-title">Your High-Quality TV<br>Installations</h1>
  <p class="abs hero-copy">At KorvanVista, we specialize in providing top-notch HD TV installations that elevate your viewing experience to the next level.</p>
  <div class="abs btn get-started">Get Started</div>
  <div class="abs learn"><span>Learn More</span>
    <svg width="16" height="10" viewBox="0 0 16 10"><path d="M0 5h14M10 1l4 4-4 4" stroke="#fff" stroke-width="1.5" fill="none"/></svg>
  </div>
  <div class="abs stats">
    <div class="stat" style="width:112px"><div class="num">10</div><div class="lbl">Partners</div></div>
    <div class="stat" style="width:92px"><div class="num">5</div><div class="lbl">Cities</div></div>
    <div class="stat"><div class="num">100+</div><div class="lbl">Customers</div></div>
  </div>
  <div class="abs hero-img" role="img" aria-label="Modern living room with wall-mounted TV, sofa and ring ceiling lights"></div>
  <div class="abs search">
    <span class="ph">Enter brand name or search screensize</span>
    <div class="btn find">
      <svg width="12" height="12" viewBox="0 0 12 12"><circle cx="5" cy="5" r="4" stroke="#fff" stroke-width="1.4" fill="none"/><path d="M8 8l3 3" stroke="#fff" stroke-width="1.4"/></svg>
      Find TV
    </div>
  </div>
</section>

<section class="partners">
  <h2 class="abs partner-title">Our Partner</h2>
  <p class="abs partner-copy">Lorem ipsum dolor sit amet, consectetur adipiscing elit, sed do eiusmod.</p>
  <div class="abs logo-row" style="left:420px"><i></i>Tallow</div>
  <div class="abs logo-row" style="left:616px"><i style="border-radius:50%"></i>Brisk</div>
  <div class="abs logo-row" style="left:797px"><i></i>Norvane</div>
  <div class="abs logo-row" style="left:1001px"><i style="border-radius:50%"></i>Quell</div>
</section>

<section class="about">
  <div class="abs about-ring"></div>
  <div class="abs about-img" role="img" aria-label="Kids sitting among stacked retro television sets"></div>
  <h2 class="abs display about-title">About <em>KorvanVista</em></h2>
  <div class="abs about-body">
    <p>At KorvanVista, we're passionate about delivering unparalleled TV installations and exceptional service to our customers. With years of experience in the industry, our team brings expertise, dedication, and a commitment to excellence to every project we undertake.</p>
    <b>Our Products and Services:</b>
    <ul>
      <li>High-definition TVs from leading brands</li>
      <li>Professional installation services for homes and businesses</li>
      <li>Customized solutions to suit your space and preferences</li>
      <li>Expert advice and support throughout the process</li>
    </ul>
    <b>Experience the Difference:</b>
    <ul>
      <li>Immerse yourself in stunning visuals with our top-of-the-line TVs</li>
      <li>Enjoy hassle-free installations by our experienced technicians</li>
      <li>Transform your space into a hub of entertainment with KorvanVista</li>
    </ul>
  </div>
  <div class="abs btn about-btn">Learn more</div>
</section>

<section class="why">
  <h2 class="abs display why-title">Why Choose Us?</h2>
  <svg class="abs" style="left:213px;top:1496px" width="15" height="15"><path d="M7.5 0v15M0 7.5h15" stroke="#fff" stroke-width="1.3"/></svg>
  <svg class="abs" style="left:1089px;top:1671px" width="15" height="15"><circle cx="7.5" cy="7.5" r="6" stroke="#fff" stroke-width="1.3" fill="none"/></svg>
  <div class="abs card" style="left:167px">
    <div class="icon"><svg width="34" height="34" viewBox="0 0 34 34" fill="none" stroke="#fff" stroke-width="1.6"><rect x="3" y="4" width="28" height="26" rx="3"/><path d="M3 10h28"/><path d="M17 14l6 3v6l-6 3-6-3v-6zM11 17l6 3 6-3M17 20v6"/></svg></div>
    <h3>Trusted professionals</h3>
    <p>Professional HD TV installations for residential and commercial spaces</p>
  </div>
  <div class="abs card" style="left:469px">
    <div class="icon"><svg width="34" height="34" viewBox="0 0 34 34" fill="none" stroke="#fff" stroke-width="1.6"><rect x="3" y="4" width="28" height="26" rx="3"/><path d="M3 10h28M13 15l-4 4 4 4M21 15l4 4-4 4M18 14l-2 10"/></svg></div>
    <h3>Personalized service</h3>
    <p>Customized solutions tailored to your specific needs</p>
  </div>
  <div class="abs card" style="left:771px">
    <div class="icon"><svg width="34" height="34" viewBox="0 0 34 34" fill="none" stroke="#fff" stroke-width="1.6"><path d="M8 22l10-12 6 6-12 10zM8 22l-3 3 4 4 3-3M20 6l2-3M26 10l3-2M24 7l2-2"/></svg></div>
    <h3>Customer satisfaction</h3>
    <p>Expert advice and guidance to help you choose the perfect setup</p>
  </div>
</section>

<section class="reviews">
  <div class="abs display ghost">Reviews</div>
  <div class="abs review-ring"></div>
  <div class="abs review-img" role="img" aria-label="Customer in neon lighting leaning on a retro television"></div>
  <h2 class="abs display review-title">Feedback from<br>Our Customers</h2>
  <p class="abs review-copy">Whether you're upgrading your home theater or enhancing your business environment, KorvanVista has you covered.</p>
  <div class="abs author">— Ilsa Marrow - CEO</div>
  <div class="abs arrow" style="left:642px;background:#ef4b2f"><svg width="10" height="8" viewBox="0 0 10 8"><path d="M9 4H1M4 1L1 4l3 3" stroke="#000" stroke-width="1.3" fill="none"/></svg></div>
  <div class="abs arrow" style="left:682px;background:#7a2a1f"><svg width="10" height="8" viewBox="0 0 10 8"><path d="M1 4h8M6 1l3 3-3 3" stroke="#000" stroke-width="1.3" fill="none"/></svg></div>
</section>

<section class="abs cta">
  <h2 class="display cta-text"><span>Contact us</span> now to schedule a consultation and take the first step towards an upgraded viewing experience!</h2>
  <div class="cta-btn">Schedule a Call</div>
</section>

<footer>
  <div class="abs brand foot-brand">KorvanVista</div>
  <p class="abs foot-tag">Ready to elevate your TV viewing experience?</p>
  <div class="abs socials"><i></i><i></i><i></i><i></i></div>
  <div class="abs copyright">Copyright©.All right reserved</div>
  <div class="abs fcol" style="left:576px"><h4>Company</h4><ul><li>About</li><li>Terms</li><li>Privacy Policy</li><li>Careers</li></ul></div>
  <div class="abs fcol" style="left:734px"><h4>Info</h4><ul><li>Select</li><li>Services</li><li>Payment</li></ul></div>
  <div class="abs fcol" style="left:909px"><h4>Contact</h4><ul><li>Call : 123-456-7890</li><li>Email : hello@korvanmail.net</li><li>Address : xyz</li></ul></div>
</footer>

</body>
</html>
```